Belmora Wines

Hi all,

My name’s Tom Welling and I run a small wine brand based in the Canberra Wine District, Australia. I’m currently in the process of branding the business and am looking for a designer to help develop a new visual direction.

Background
I’ll be growing my own fruit from a leased vineyard site Named 'Ashbrook' and my family’s property named 'Tallin Park', with a stronger emphasis on organic practices and site expression.

The Direction
The brand will centre around single vineyard wines, with each wine reflecting the unique site it comes from. I’d like the branding to support this idea of place, origin, and authenticity.

In terms of visual style, I’m drawn to something that is:

Simple and effective
A balance between traditional and modern
Clean, considered, and not overly decorative

Nothing too over-the-top, the goal is something timeless that lets the wine and vineyard story speak for itself.

At this stage, I’m mainly looking for:

Conceptual design direction / ideas
Label design (with potential to expand into broader branding)

I’m open to creative interpretation, so if the story resonates with you, I’d love to see how you would approach it.

Below I've attached an example of the bottle shape I will be using.

Cheers,
Tom

Colors
0054AA
0677BA
7BADD7
CADEEF
E8F1F8
FFC000
F8CF3A
FAE287
FDF2CF
FEFAEE

Requirements
Must have
• Mix of modern and traditional

```html
<!DOCTYPE html>
<html lang="en">
<head>
<meta charset="utf-8">
<title>Belmora Wines — Shiraz Label</title>
<link rel="stylesheet" href="https://fonts.googleapis.com/css2?family=Libre+Baskerville:wght@400&family=Jost:wght@400&display=swap">
<style>
  :root {
    --blue-deep: #0054AA;
    --blue: #0677BA;
    --blue-soft: #7BADD7;
    --blue-pale: #CADEEF;
    --blue-mist: #E8F1F8;
    --gold: #FFC000;
    --gold-soft: #F8CF3A;
    --gold-pale: #FAE287;
    --cream: #FDF2CF;
    --paper: #FEFAEE;
    --ink: #1c2a3a;
    --ink-soft: #2f3d4d;
  }
  * { margin: 0; padding: 0; box-sizing: border-box; }
  html, body {
    width: 800px;
    height: 1200px;
    overflow: hidden;
    background: var(--blue-mist);
  }
  .canvas {
    width: 800px;
    height: 1200px;
    display: flex;
    align-items: center;
    justify-content: center;
  }
  .label {
    position: relative;
    width: 720px;
    height: 660px;
    background: var(--paper);
    border: 1px solid var(--blue-pale);
    color: var(--ink);
    text-align: center;
  }
  .label__producer {
    position: absolute;
    top: 70px;
    left: 0;
    right: 0;
    font-family: "Libre Baskerville", Georgia, serif;
    font-weight: 400;
    font-size: 27px;
    letter-spacing: 0.06em;
    text-transform: uppercase;
    color: var(--ink);
  }
  .label__artwork {
    position: absolute;
    top: 140px;
    left: 80px;
    width: 560px;
    height: 210px;
    border-radius: 6px;
    background:
      radial-gradient(ellipse at 50% 30%, var(--blue-soft) 0%, rgba(123,173,215,0) 14%),
      radial-gradient(ellipse at 50% 60%, var(--blue-pale) 0%, var(--cream) 55%, var(--paper) 90%);
  }
  .label__variety {
    position: absolute;
    top: 382px;
    left: 0;
    right: 0;
    font-family: "Libre Baskerville", Georgia, serif;
    font-weight: 400;
    font-size: 64px;
    line-height: 1;
    color: var(--ink);
  }
  .label__site {
    position: absolute;
    top: 480px;
    left: 0;
    right: 0;
    font-family: "Jost", Arial, sans-serif;
    font-size: 26px;
    line-height: 46px;
    letter-spacing: 0.05em;
    text-transform: uppercase;
    color: var(--ink-soft);
  }
  .label__credentials {
    position: absolute;
    top: 596px;
    left: 0;
    right: 0;
    font-family: "Jost", Arial, sans-serif;
    font-size: 18px;
    letter-spacing: 0.06em;
    text-transform: uppercase;
    color: var(--ink-soft);
  }
  .label__bullet { color: var(--gold); }
</style>
</head>
<body>
  <main class="canvas">
    <section class="label">
      <h1 class="label__producer">Belmora Wines</h1>
      <div class="label__artwork" role="img" aria-label="Ink sketch of a duck with a coloured head spreading its wings beside an old wagon wheel and a winding creek"></div>
      <h2 class="label__variety">Shiraz</h2>
      <p class="label__site">Ashbrook Vineyard<br>Canberra District</p>
      <p class="label__credentials">Organically Farmed <span class="label__bullet">&bull;</span> Single Vineyard</p>
    </section>
  </main>
</body>
</html>
```